New Website Deisgn. Guaranteed Project.

I would like a site similar to this: http://givewheelsheal.org.

old site: http://autosforrelief.org

Create a professional website; a car donation site seeking leads to return calls.

Please see http://givewheelsheal.org for the concept I am after.

The webpage should have a professional feel. The pages to include are 'Home', 'About us' and 'Get Started'

Industry/Entity Type

It Professional

Coding

Coded - Design and coding required

Number of Pages Required

1 page

```html
<!DOCTYPE html>
<html lang="en">
<head>
<meta charset="utf-8">
<title>Hope Harbor Kids Foundation – Donate Car to Charity</title>
<link rel="stylesheet" href="https://fonts.googleapis.com/css2?family=Montserrat:wght@500;600;700&family=Open+Sans:wght@400;600;700&family=Raleway:wght@400;500&display=swap">
<style>
:root{
  --teal:#0f8a86;
  --teal-dark:#0b7774;
  --teal-light:#169a96;
  --ink:#2c2c2c;
  --muted:#666;
  --hero-top:#f3f3f3;
  --hero-bottom:#d6d6d6;
  --ring:#dcdcdc;
  --footer:#474747;
  --white:#fff;
}
*{box-sizing:border-box;margin:0;padding:0}
html,body{width:1200px;height:2247px;overflow:hidden;background:var(--white)}
body{position:relative;font-family:"Open Sans",Arial,sans-serif;color:var(--ink)}
.abs{position:absolute}

/* header */
.site-header{left:0;top:0;width:1200px;height:114px;background:var(--white)}
.brand{left:130px;top:28px;display:flex;align-items:center;gap:10px}
.brand-mark{width:44px;height:44px;border-radius:50%;background:var(--teal)}
.brand-name{font-family:"Open Sans",sans-serif;font-weight:600;font-size:14px;line-height:17px;color:var(--teal-dark);width:110px}
.main-nav{left:0;top:114px;width:1200px;height:48px;background:linear-gradient(var(--teal-light),var(--teal-dark))}
.main-nav a{position:absolute;top:14px;color:var(--white);font-weight:700;font-size:15px;text-decoration:none}

/* hero */
.hero{left:0;top:162px;width:1200px;height:386px;background:linear-gradient(var(--hero-top),var(--hero-bottom))}
.hero-visual{left:345px;top:225px;width:340px;height:323px;background:radial-gradient(ellipse at 55% 65%,#b8b8b8,#dcdcdc 60%,rgba(220,220,220,0) 80%)}
.hero-title{left:132px;top:268px;font-family:"Montserrat",sans-serif;font-weight:600;font-size:32px;letter-spacing:1.5px;color:#333}
.hero-sub{left:132px;top:322px;font-family:"Montserrat",sans-serif;font-weight:500;font-size:20px;letter-spacing:1.2px;color:#444}
.btn-details{left:132px;top:373px;width:126px;height:41px;background:var(--teal);color:var(--white);font-size:11px;font-weight:700;display:flex;align-items:center;justify-content:center;border-radius:2px}
.dots{left:131px;top:446px;display:flex;gap:8px}
.dots span{width:10px;height:10px;border-radius:50%;background:#b5b5b5}
.dots span:first-child{background:var(--white)}

/* donate panel */
.donate-panel{left:684px;top:52px;width:384px;height:496px}
.donate-panel svg{position:absolute;left:0;top:0}
.panel-call{left:684px;top:124px;width:384px;text-align:center;color:var(--white);font-family:"Montserrat",sans-serif;font-weight:500;font-size:20px;letter-spacing:1px}
.panel-phone{left:684px;top:156px;width:384px;text-align:center;color:var(--white);font-family:"Montserrat",sans-serif;font-weight:700;font-size:25px;letter-spacing:1px}
.panel-note{left:684px;top:199px;width:384px;text-align:center;color:var(--white);font-weight:700;font-size:14px}
.field{height:43px;background:var(--white);border-radius:3px;font-size:11px;color:#777;display:flex;align-items:center;padding-left:12px}
.field svg{position:absolute;right:14px;top:17px}
.btn-donate{left:711px;top:470px;width:332px;height:48px;background:linear-gradient(#3a3a3a,#1c1c1c);border-radius:3px;color:var(--white);font-family:"Montserrat",sans-serif;font-weight:700;font-size:19px;display:flex;align-items:center;justify-content:center;letter-spacing:.5px}

/* features */
.section-title{left:0;width:1200px;text-align:center;font-family:"Montserrat",sans-serif;font-weight:600;font-size:32px;color:var(--teal)}
.feature{width:300px;text-align:center}
.feature svg{display:block;margin:0 auto}
.feature h3{font-family:"Raleway",sans-serif;font-weight:500;font-size:20px;color:#222;margin-top:22px}
.feature p{font-size:10.5px;line-height:24px;color:#555;margin:14px auto 0;width:250px}

/* faq */
.faq{left:0;top:1170px;width:1200px;height:516px;background:linear-gradient(115deg,#12928e,#0d807c 45%,#13918d 70%,#0c7b77)}
.faq-title{left:131px;top:1246px;color:var(--white);font-family:"Montserrat",sans-serif;font-weight:700;font-size:32px}
.faq-q{color:var(--white);font-family:"Raleway",sans-serif;font-size:20px}
.faq-a{left:131px;top:1360px;width:930px;color:var(--white);font-size:10.5px;line-height:22px}
.faq-list{left:131px;top:1421px;list-style:none}
.faq-list li{color:var(--white);font-family:"Raleway",sans-serif;font-size:20px;line-height:29px}

/* steps */
.step-ring{width:104px;height:104px;border-radius:50%;border:7px solid var(--ring);display:flex;align-items:center;justify-content:center;background:var(--white)}
.step{width:260px;text-align:center}
.step h3{font-family:"Montserrat",sans-serif;font-weight:600;font-size:19px;color:#222}
.step p{font-size:11.5px;line-height:20px;color:#555;width:220px;margin:14px auto 0}

/* footer */
.site-footer{left:0;top:2106px;width:1200px;height:141px;background:var(--footer)}
.social{left:534px;top:2137px;display:flex;gap:10px}
.social span{width:24px;height:24px;border-radius:50%;background:#8a8a8a}
.footer-links{left:0;top:2174px;width:1200px;text-align:center;color:var(--white);font-size:11px}
.copyright{left:0;top:2202px;width:1200px;text-align:center;color:var(--white);font-size:11px}
</style>
</head>
<body>

<header class="abs site-header">
  <div class="abs brand">
    <span class="brand-mark"></span>
    <span class="brand-name">Hope Harbor Kids Foundation</span>
  </div>
</header>

<nav class="abs main-nav">
  <a href="#" style="left:133px">How It Works</a>
  <a href="#" style="left:277px">Charities</a>
  <a href="#" style="left:388px">Tax Deduction</a>
  <a href="#" style="left:540px">FAQ</a>
</nav>

<section class="abs hero"></section>
<div class="abs hero-visual" role="img" aria-label="Photo of a hand holding car keys in front of a silver car"></div>
<h1 class="abs hero-title">Donate Car to Charity!</h1>
<p class="abs hero-sub">Your car can make a difference!</p>
<div class="abs btn-details">VIEW DETAILS</div>
<div class="abs dots"><span></span><span></span><span></span></div>

<aside class="abs donate-panel">
  <svg width="384" height="496" viewBox="0 0 384 496"><path d="M0 0 L192 48 L384 0 V496 H0 Z" fill="#0f8a86"/></svg>
</aside>
<div class="abs panel-call">Call Today to Donate</div>
<div class="abs panel-phone">1-800-555-0142</div>
<div class="abs panel-note">Or Fill out the form below to instantly donate online</div>
<div class="abs field" style="left:710px;top:251px;width:158px">First Name</div>
<div class="abs field" style="left:881px;top:251px;width:159px">Last Name</div>
<div class="abs field" style="left:710px;top:302px;width:330px">Phone Number</div>
<div class="abs field" style="left:710px;top:355px;width:330px">Email Address</div>
<div class="abs field" style="left:710px;top:408px;width:158px">Make of Car<svg width="13" height="8" viewBox="0 0 13 8"><path d="M1 1l5.5 5.5L12 1" stroke="#333" stroke-width="1.6" fill="none"/></svg></div>
<div class="abs field" style="left:881px;top:408px;width:159px">Model of Car<svg width="13" height="8" viewBox="0 0 13 8"><path d="M1 1l5.5 5.5L12 1" stroke="#333" stroke-width="1.6" fill="none"/></svg></div>
<div class="abs btn-donate">DONATE NOW</div>

<h2 class="abs section-title" style="top:592px">Why Autosforrelief</h2>

<div class="abs feature" style="left:110px;top:678px">
  <svg width="30" height="44" viewBox="0 0 30 44"><path d="M15 0C6.7 0 0 6.7 0 15c0 11 15 29 15 29s15-18 15-29C30 6.7 23.3 0 15 0z" fill="#0f8a86"/><circle cx="15" cy="15" r="5.5" fill="#fff"/></svg>
  <h3>Free Local Towing</h3>
  <p>We will pick up your car donation when it's most convenient for you either at home or work at</p>
</div>
<div class="abs feature" style="left:450px;top:678px">
  <svg width="42" height="44" viewBox="0 0 42 44"><path d="M0 0H42V28L28 42H0Z" fill="#0f8a86"/><path d="M28 42V28H42" fill="#fff"/></svg>
  <h3>No Paperwork Hassles</h3>
  <p>We will pick up your car donation when it's most convenient for you either at home or work at</p>
</div>
<div class="abs feature" style="left:789px;top:678px">
  <svg width="56" height="44" viewBox="0 0 56 44"><path d="M12 6Q14 0 20 0H36Q42 0 44 6L48 18H52Q56 18 56 22V34H50V42H42V34H14V42H6V34H0V22Q0 18 4 18H8Z" fill="#0f8a86"/><path d="M14 18L17 8H39L42 18Z" fill="#fff"/><circle cx="10" cy="26" r="3.5" fill="#fff"/><circle cx="46" cy="26" r="3.5" fill="#fff"/></svg>
  <h3>Accept All Cars</h3>
  <p>We will pick up your car donation when it's most convenient for you either at home or work at</p>
</div>

<div class="abs feature" style="left:110px;top:900px">
  <svg width="50" height="44" viewBox="0 0 50 44"><path d="M17 4Q17 0 21 0H29Q33 0 33 4V8H29V4H21V8H17Z" fill="#0f8a86"/><rect x="0" y="9" width="50" height="35" rx="3" fill="#0f8a86"/><rect x="0" y="23" width="50" height="3" fill="#fff"/><rect x="21" y="20" width="8" height="9" fill="#fff"/></svg>
  <h3>Income Tax Deduction</h3>
  <p>We will pick up your car donation when it's most convenient for you either at home or work at</p>
</div>
<div class="abs feature" style="left:450px;top:900px">
  <svg width="42" height="48" viewBox="0 0 42 48"><ellipse cx="21" cy="7" rx="21" ry="7" fill="#0f8a86"/><path d="M0 12Q21 22 42 12V22Q21 32 0 22Z" fill="#0f8a86"/><path d="M0 26Q21 36 42 26V36Q21 46 0 36Z" fill="#0f8a86"/><path d="M0 40Q21 50 42 40V41Q21 51 0 41Z" fill="#0f8a86"/></svg>
  <h3>Help fund Programs</h3>
  <p>We will pick up your car donation when it's most convenient for you either at home or work at</p>
</div>
<div class="abs feature" style="left:789px;top:900px">
  <svg width="48" height="48" viewBox="0 0 48 48"><g transform="rotate(45 24 24)"><rect x="10" y="2" width="28" height="14" rx="2" fill="#0f8a86"/><rect x="20" y="16" width="8" height="30" rx="2" fill="#0f8a86"/></g></svg>
  <h3>Largest Auction</h3>
  <p>We will pick up your car donation when it's most convenient for you either at home or work at</p>
</div>

<section class="abs faq" role="img" aria-label="Faint background photo of hands exchanging car keys, tinted teal"></section>
<h2 class="abs faq-title">FAQ</h2>
<p class="abs faq-q" style="left:131px;top:1317px">What types of vehicles can be donated?</p>
<p class="abs faq-a">Nemo enim ipsam voluptatem quia voluptas sit aspernatur aut odit aut fugit, sed quia consequuntur magni dolores eos qui ratione voluptatem sequi nesciunt. Neque porro quisquam est, qui dolorem ipsum quia dolor sit amet, consectetur, adipisci velit, sed quia non numquam eius modi tempora incidunt</p>
<ul class="abs faq-list">
  <li>If my vehicle is not running, can I still donate?</li>
  <li>What paperwork do I need to donate my vehicle?</li>
  <li>Is my donated vehicle tax -deductible?</li>
  <li>What areas do you service?</li>
  <li>What documents do I need to donate a car to charity?</li>
  <li>What if the vehicle is not registered in my name?</li>
</ul>

<h2 class="abs section-title" style="top:1740px">How it Works</h2>

<div class="abs step-ring" style="left:186px;top:1816px">
  <svg width="46" height="42" viewBox="0 0 46 42"><path d="M30 6H6Q3 6 3 9V36Q3 39 6 39H33Q36 39 36 36V22" stroke="#0f8a86" stroke-width="4" fill="none"/><path d="M38 2L44 8L24 28L16 30L18 22Z" fill="#0f8a86"/></svg>
</div>
<div class="abs step-ring" style="left:548px;top:1816px">
  <svg width="56" height="44" viewBox="0 0 56 44"><path d="M12 6Q14 0 20 0H36Q42 0 44 6L48 18H52Q56 18 56 22V34H50V42H42V34H14V42H6V34H0V22Q0 18 4 18H8Z" fill="#0f8a86"/><path d="M14 18L17 8H39L42 18Z" fill="#fff"/><circle cx="10" cy="26" r="3.5" fill="#fff"/><circle cx="46" cy="26" r="3.5" fill="#fff"/></svg>
</div>
<div class="abs step-ring" style="left:900px;top:1823px">
  <svg width="44" height="48" viewBox="0 0 44 48"><path d="M0 0H22L30 8V36H0Z" fill="#0f8a86"/><path d="M12 12H34L44 22V48H12Z" fill="#0f8a86" stroke="#fff" stroke-width="3"/><path d="M34 12V22H44" fill="#fff"/></svg>
</div>

<svg class="abs" style="left:340px;top:1858px" width="180" height="60" viewBox="0 0 180 60"><path d="M6 32Q60 70 165 10" stroke="#333" stroke-width="2" stroke-dasharray="6 5" fill="none"/><path d="M168 6L153 10L162 20Z" fill="#333"/></svg>
<svg class="abs" style="left:700px;top:1858px" width="180" height="60" viewBox="0 0 180 60"><path d="M6 32Q60 70 165 10" stroke="#333" stroke-width="2" stroke-dasharray="6 5" fill="none"/><path d="M168 6L153 10L162 20Z" fill="#333"/></svg>

<div class="abs step" style="left:108px;top:1958px">
  <h3>Fill out the simple form</h3>
  <p>Use our online vehicle donation form to submit your information.Vehicle donations accepted nationwide</p>
</div>
<div class="abs step" style="left:470px;top:1958px">
  <h3>Schedule your pick-up</h3>
  <p>Use our online vehicle donation form to submit your information.Vehicle donations accepted nationwide</p>
</div>
<div class="abs step" style="left:826px;top:1958px">
  <h3>Receive tax deduction</h3>
  <p>Use our online vehicle donation form to submit your information.Vehicle donations accepted nationwide</p>
</div>

<footer class="abs site-footer"></footer>
<div class="abs social"><span></span><span></span><span></span><span></span></div>
<p class="abs footer-links">About us | Charities | FAQ | Privacy Policy</p>
<p class="abs copyright">©Copyright 2017 Hope Harbor Kids Foundation</p>

</body>
</html>
```